Petal Crest Arbour Rentals Spain

Why not add the WOW factor to your special occassion by bringing it to life with our beautiful selection of magnificent Blosom Tree´s.
Handmade with Silk Flowers these Tree´s look real to life adding the perfect decoration to your event or breathtaking feature for your Wedding Day.
Our Tree´s suit any theme whether its Rustic, Elegant, Fairy Tale or Enhanted.
With a versitle selection we offerf floor to ceiling and table centre pieces which can be used both inside or outdoor.
If you are looking for your Fiary Tale look no further.
Target Market(s)
Franchise , weddings and Events
Font styles to use
Requirements
Must have
- Crisp Lettering and attractive Presintation
Nice to have
- Elegant fonts and different from the rest
I am looking for a overall branding design ,including letter heads Buisness cards email signuture a4 template design ,invoising design ,Presentation folder design to hold A4 papers and usb stick ,envolope design ,flyier design ,three font designs sticker design, New logo design 3 concepts

```html
<!DOCTYPE html>
<html lang="en">
<head>
<meta charset="utf-8">
<title>Petal Crest Arbour Rentals – Presentation Folder</title>
<link href="https://fonts.googleapis.com/css2?family=Cinzel:wght@400&family=Great+Vibes&family=Josefin+Sans:wght@400&display=swap" rel="stylesheet">
<style>
  :root {
    --stage: #cbcbcb;
    --paper: #ffffff;
    --gold: #c39a3e;
    --blush: #d5b6ab;
    --rose: #e07ab8;
    --ink: #1f1f1f;
    --usb-edge: #9a9a9a;
  }
  * { margin: 0; padding: 0; box-sizing: border-box; }
  html, body { width: 1200px; height: 600px; overflow: hidden; }
  body { background: var(--stage); position: relative; font-family: "Josefin Sans", sans-serif; }

  .usb {
    position: absolute; top: 29px; width: 159px; height: 48px;
    background: var(--paper); border-radius: 6px;
    box-shadow: 1px 2px 3px rgba(0,0,0,.35);
  }
  .usb--left { left: 324px; }
  .usb--right { left: 675px; }
  .usb__divider { position: absolute; top: 0; bottom: 0; width: 1px; background: var(--usb-edge); }
  .usb--left .usb__divider { left: 115px; }
  .usb--right .usb__divider { left: 45px; }
  .usb__hole { position: absolute; top: 21px; width: 7px; height: 5px; border-radius: 50%; background: #000; }
  .usb--left .usb__hole { left: 3px; }
  .usb--right .usb__hole { right: 3px; }
  .usb__name { position: absolute; top: 14px; width: 80px; text-align: center; color: var(--gold); font-family: "Cinzel", serif; line-height: 1; }
  .usb--left .usb__name { left: 22px; }
  .usb--right .usb__name { left: 55px; }
  .usb__name-main { display: block; font-size: 10px; letter-spacing: .3px; }
  .usb__name-sub { display: block; font-size: 5.3px; margin-top: 2px; }

  .panel {
    position: absolute; top: 105px; width: 328px; height: 461px;
    background: var(--paper); box-shadow: 2px 3px 4px rgba(0,0,0,.35); overflow: hidden;
  }
  .panel--cover { left: 60px; }
  .panel--inside { left: 418px; }
  .panel--back { left: 777px; }

  .cover__photo {
    position: absolute; inset: 0;
    background:
      radial-gradient(ellipse 60% 25% at 50% 18%, #f6d9cf 0%, rgba(246,217,207,0) 100%),
      linear-gradient(180deg, #d9a898 0%, #e9c3ba 22%, #d9b1a6 45%, #3a3133 62%, #4a3d40 80%, #8c6d6c 100%);
  }
  .cover__name { position: absolute; left: 0; right: 0; top: 320px; text-align: center; color: var(--gold); font-family: "Cinzel", serif; line-height: 1; }
  .cover__name-main { display: block; font-size: 19px; letter-spacing: .5px; }
  .cover__name-sub { display: block; font-size: 10px; margin-top: 3px; }

  .inside__wave { position: absolute; left: 0; top: 0; width: 328px; height: 461px; }

  .back__mark { position: absolute; top: 178px; left: 0; right: 0; text-align: center; }
  .back__dot { width: 22px; height: 22px; border-radius: 50%; background: var(--rose); margin: 0 auto 10px; }
  .back__name { color: var(--gold); font-family: "Cinzel", serif; line-height: 1.15; font-size: 17px; }
  .back__address {
    position: absolute; top: 318px; left: 0; right: 0; text-align: center;
    font-family: "Great Vibes", cursive; font-size: 18px; line-height: 22px; color: var(--ink);
  }
  .back__contacts {
    position: absolute; bottom: 11px; left: 12px; right: 8px;
    display: flex; justify-content: space-between; align-items: center;
    font-size: 6.2px; color: var(--ink); white-space: nowrap;
  }
  .contact { display: flex; align-items: center; gap: 3px; }
  .contact__icon { width: 7px; height: 7px; flex: none; }
  .contact__square { width: 6px; height: 6px; background: var(--gold); flex: none; }
</style>
</head>
<body>
  <div class="usb usb--left">
    <span class="usb__hole"></span>
    <div class="usb__name"><span class="usb__name-main">PETAL CREST</span><span class="usb__name-sub">ARBOUR RENTALS</span></div>
    <span class="usb__divider"></span>
  </div>
  <div class="usb usb--right">
    <span class="usb__divider"></span>
    <div class="usb__name"><span class="usb__name-main">PETAL CREST</span><span class="usb__name-sub">ARBOUR RENTALS</span></div>
    <span class="usb__hole"></span>
  </div>

  <section class="panel panel--cover">
    <div class="cover__photo" role="img" aria-label="Photo of a candlelit wedding aisle under arching pink blossom trees on a reflective floor"></div>
    <div class="cover__name"><span class="cover__name-main">PETAL CREST</span><span class="cover__name-sub">ARBOUR RENTALS</span></div>
  </section>

  <section class="panel panel--inside">
    <svg class="inside__wave" viewBox="0 0 328 461" aria-hidden="true">
      <path d="M2 461 C10 385 45 345 135 343 L328 343 L328 461 Z" fill="var(--blush)"/>
    </svg>
  </section>

  <section class="panel panel--back">
    <div class="back__mark">
      <div class="back__dot"></div>
      <div class="back__name">PETAL CREST<br>ARBOUR RENTALS</div>
    </div>
    <div class="back__address">Visit our showroom<br>Calle Olivos 12<br>Villa Serena<br>Andalucia Spain</div>
    <div class="back__contacts">
      <span class="contact">
        <svg class="contact__icon" viewBox="0 0 10 8"><rect width="10" height="8" fill="var(--gold)"/><path d="M0 0 L5 4.5 L10 0" fill="none" stroke="#fff" stroke-width="1"/></svg>
        info@petalcrestarbour.com
      </span>
      <span class="contact">
        <svg class="contact__icon" viewBox="0 0 6 10"><rect x=".5" y=".5" width="5" height="9" rx="1" fill="none" stroke="var(--gold)" stroke-width="1"/></svg>
        600123456
      </span>
      <span class="contact"><span class="contact__square"></span>@petalcrestspain</span>
      <span class="contact"><span class="contact__square"></span>petalcrest_spain</span>
    </div>
  </section>
</body>
</html>
```